Business card for a new cabinet shop company named Marlowe Cabinets for high end cabinets

Design a business card, thinking dark rich green with colours to speak of high end luxury ie; cream, gold, black possibly

Peter Lindqvar
Director Craftsman
Email: info@marlowecabinets.com.au
Instagram : @marlowe.cabinets

```html
<!DOCTYPE html>
<html lang="en">
<head>
<meta charset="utf-8">
<title>Marlowe Cabinets — Business Card</title>
<link rel="stylesheet" href="https://fonts.googleapis.com/css2?family=Montserrat:wght@300;400;500;700&display=swap">
<style>
  :root {
    --stage: #2c2c2c;
    --stage-dark: #121212;
    --card: #1c1c1c;
    --card-edge: #2a2a2a;
    --pattern-dark: #111111;
    --pattern-light: #2e2e2e;
    --gold: #c9a45c;
    --white: #f4f2ee;
    --green: #6f9a5a;
    --muted: #d8d6d2;
  }
  * { margin: 0; padding: 0; box-sizing: border-box; }
  html, body { width: 1200px; height: 875px; overflow: hidden; }
  body {
    background: linear-gradient(160deg, var(--stage) 0%, var(--stage-dark) 100%);
    font-family: "Montserrat", sans-serif;
    position: relative;
  }
  .card {
    position: absolute;
    border-radius: 20px;
    background: var(--card);
    border: 1px solid var(--card-edge);
    box-shadow: 0 26px 54px rgba(0,0,0,0.6);
    overflow: hidden;
  }

  /* Back of card */
  .card-back { left: 60px; top: 80px; width: 500px; height: 286px; }
  .card-back .pattern {
    position: absolute; inset: 0;
    background: linear-gradient(110deg, var(--pattern-light) 0%, var(--pattern-dark) 42%, #181818 100%);
  }
  .card-back .wordmark {
    position: absolute; right: 40px; top: 118px;
  }
  .card-back .wordmark-mark { width: 30px; height: 30px; }
  .card-back .wordmark-text { font-size: 24px; }

  /* Shared wordmark */
  .wordmark { display: flex; align-items: center; gap: 16px; }
  .wordmark-mark { background: var(--gold); flex: none; }
  .wordmark-text {
    color: var(--gold);
    font-weight: 500;
    line-height: 1;
    white-space: nowrap;
  }

  /* Front of card */
  .card-front { left: 560px; top: 450px; width: 590px; height: 337px; }
  .card-front .sheen {
    position: absolute; left: 0; top: 0; bottom: 0; width: 110px;
    background: linear-gradient(90deg, rgba(255,255,255,0.07), rgba(255,255,255,0));
  }
  .card-front .wordmark { position: absolute; left: 70px; top: 52px; gap: 26px; }
  .card-front .wordmark-mark { width: 92px; height: 92px; }
  .card-front .wordmark-text { font-size: 50px; line-height: 1.05; }

  .details {
    position: absolute; left: 70px; top: 208px;
    display: flex; align-items: center; gap: 20px;
  }
  .person { text-align: right; }
  .person-name { font-size: 22px; color: var(--white); white-space: nowrap; }
  .person-name .first { font-weight: 700; }
  .person-name .last { font-weight: 300; color: var(--green); }
  .person-role { font-size: 12px; font-weight: 400; color: var(--muted); margin-top: 4px; }
  .divider { width: 1px; height: 78px; background: var(--green); }
  .contact { list-style: none; font-size: 13px; color: var(--muted); }
  .contact li { display: flex; align-items: center; gap: 9px; line-height: 25px; white-space: nowrap; }
  .contact .icon { width: 13px; height: 13px; flex: none; }
  .contact .location { font-size: 15px; color: var(--white); }
</style>
</head>
<body>

<section class="card card-back" aria-label="Card back">
  <div class="pattern" role="img" aria-label="Repeating embossed gloss monogram pattern across the card"></div>
  <div class="wordmark">
    <span class="wordmark-mark"></span>
    <span class="wordmark-text">Marlowe Cabinets</span>
  </div>
</section>

<section class="card card-front" aria-label="Card front">
  <div class="sheen"></div>
  <div class="wordmark">
    <span class="wordmark-mark"></span>
    <span class="wordmark-text">Marlowe<br>Cabinets</span>
  </div>

  <div class="details">
    <div class="person">
      <p class="person-name"><span class="first">Peter</span> <span class="last">Lindqvar</span></p>
      <p class="person-role">Director Craftsman</p>
    </div>
    <span class="divider"></span>
    <ul class="contact">
      <li>
        <svg class="icon" viewBox="0 0 12 12" aria-hidden="true">
          <rect x="0.5" y="2" width="11" height="8" fill="var(--green)"/>
          <path d="M0.5 2 L6 6.5 L11.5 2" fill="none" stroke="#1c1c1c" stroke-width="1"/>
        </svg>
        info@marlowecabinets.com.au
      </li>
      <li>
        <svg class="icon" viewBox="0 0 12 12" aria-hidden="true">
          <circle cx="6" cy="6" r="5.5" fill="var(--green)"/>
        </svg>
        @marlowe.cabinets
      </li>
      <li class="location">Westhaven Coast</li>
    </ul>
  </div>
</section>

</body>
</html>
```